Expense Tracker App for Young Adults

I need a mobile app designer to design an app UI for me. It is for an expense tracker app. I’ve attached a mind map of the various screens and features of the app.

I would like to see designs for this app which is targeted towards young adults (late teens & early 20s) just starting their career who want to plan their budgets and track their expenses.
Updates

Hello designers! I'm conscious that this is not a guaranteed project, so I can understand that some of you might be apprehensive. Just wanted to let you know that I'm willing to see your initial drafts that show your direction and theme for design. You don't have to design the whole app. In fact, it's better if you share your initial design ideas so that we can have a discussion and I can give my input. If I see some good initial designs, I will be happy to make this a guaranteed project. I'm simply being cautious since I'm bootstrapping this and funding out of my own pocket. Thank you for your understanding!

Target Market(s)

Young adults who are just starting their careers, late teens and early 20s.

Font styles to use
Sans Serif

Requirements
Must have
• Ease of use, smart and sleek, a guided setup wizard which will help users setup their account after signing up.
Should not have
• Clunky

```html
<!DOCTYPE html>
<html lang="en">
<head>
<meta charset="utf-8">
<title>Expenses Tracker – App Screens</title>
<link href="https://fonts.googleapis.com/css2?family=Open+Sans:wght@400;600;700&display=swap" rel="stylesheet">
<style>
:root{
  --bg:#9cc3f8;
  --bg-blob:#86a8d8;
  --navy:#1a3a78;
  --navy-dark:#0f2a55;
  --panel:#f2f2f8;
  --lilac:#e3e0f2;
  --field:#e6e3f4;
  --green:#1f8a3e;
  --red:#e0203a;
  --white:#ffffff;
  --ink:#222a3a;
  --muted:#6b7280;
  --black:#050505;
  --tab-off:#a3b3d9;
}
*{box-sizing:border-box;margin:0;padding:0}
html,body{width:1200px;height:1029px;overflow:hidden;background:var(--bg);font-family:"Open Sans",sans-serif}
.canvas{position:relative;width:1200px;height:1029px;overflow:hidden;background:var(--bg)}
.stage{position:absolute;left:0;top:0;width:2072px;height:1776px;transform:scale(0.5792);transform-origin:0 0}
.blob{position:absolute;border-radius:50%;background:var(--bg-blob)}
.phone{position:absolute;width:333px;height:722px;background:var(--panel);overflow:hidden;box-shadow:0 6px 18px rgba(20,40,90,.18)}
.status{position:absolute;left:0;top:0;width:100%;height:23px;background:var(--navy-dark);color:#fff;font-size:13px;font-weight:600;padding:3px 0 0 19px}
.status svg{position:absolute;right:20px;top:6px}
.header{position:absolute;left:0;top:23px;width:100%;height:100px;background:var(--navy)}
.avatar{position:absolute;left:10px;top:19px;width:32px;height:32px;border-radius:50%;background:radial-gradient(circle at 50% 40%,#d9b59a,#6b4a3a);border:2px solid #fff}
.user-name{position:absolute;left:52px;top:24px;color:#fff;font-size:16px}
.gear{position:absolute;right:12px;top:25px}
.panel{position:absolute;left:0;top:93px;width:100%;bottom:0;background:var(--panel);border-radius:16px 16px 0 0}
.abs{position:absolute}
.navbar{position:absolute;left:0;top:662px;width:100%;height:60px;background:#fff;border-radius:14px 14px 0 0;box-shadow:0 -3px 8px rgba(0,0,0,.08)}
.nav-item{position:absolute;top:12px;width:50px;margin-left:-25px;text-align:center;font-size:7.5px;color:var(--ink)}
.nav-item svg{display:block;margin:0 auto 1px}
.nav-item.active{color:#2b5bb8}
.nav-add{position:absolute;left:143px;top:9px;width:38px;height:38px;border-radius:50%;background:var(--navy);box-shadow:0 3px 6px rgba(0,0,0,.25)}
.nav-add::before,.nav-add::after{content:"";position:absolute;left:50%;top:50%;background:#fff;transform:translate(-50%,-50%)}
.nav-add::before{width:18px;height:2.5px}.nav-add::after{width:2.5px;height:18px}

/* home */
.balance-card{left:15px;top:110px;width:303px;height:80px;background:var(--lilac);border-radius:14px}
.balance-amount{left:153px;top:120px;font-size:16px;color:var(--ink)}
.balance-label{left:153px;top:142px;font-size:9px;color:var(--ink);letter-spacing:.5px}
.progress{left:27px;top:166px;width:280px;height:10px;background:#fff;border-radius:5px;overflow:hidden}
.progress span{display:block;width:81%;height:100%;background:var(--green)}
.flow{top:193px;height:75px;width:152px;color:#fff}
.flow.income{left:15px;background:var(--green);border-radius:12px 0 0 12px}
.flow.expense{left:166px;background:var(--red);border-radius:0 12px 12px 0}
.flow svg{position:absolute;left:30px;top:20px}
.flow .amt{position:absolute;left:62px;top:21px;font-size:12px}
.flow .lbl{position:absolute;left:62px;top:39px;font-size:8.5px;letter-spacing:.6px}
.flow.expense svg{left:28px}.flow.expense .amt,.flow.expense .lbl{left:68px}
.section-head{left:15px;width:303px;height:60px;background:var(--lilac);border-radius:14px}
.section-title{position:absolute;left:29px;top:9px;font-size:16px;font-weight:700;color:var(--navy);letter-spacing:.5px}
.view-all{position:absolute;left:204px;top:7px;width:68px;height:22px;border-radius:11px;background:#fff;font-size:9px;text-align:center;line-height:22px;color:var(--ink)}
.section-body{left:15px;width:303px;background:var(--navy);border-radius:14px}
.row-card{left:30px;width:273px;height:64px;background:#fff;border-radius:12px}
.row-icon{position:absolute;left:15px;top:17px;width:30px;height:30px;border-radius:50%;background:#d5dbea}
.row-icon svg{position:absolute;left:7px;top:7px}
.row-title{position:absolute;left:56px;top:23px;font-size:12.5px;color:var(--navy)}
.row-amt{position:absolute;right:50px;top:20px;font-size:16px;color:var(--red)}
.row-go{position:absolute;right:14px;top:22px}
.row-sub{position:absolute;left:56px;top:38px;font-size:5.5px;color:var(--muted)}
.trend{position:absolute;left:193px;font-size:6.5px;color:var(--ink)}
.trend b{font-weight:700}

/* history */
.timeline{left:19px;top:118px;width:2px;height:560px;background:var(--navy)}
.tx{left:36px;width:280px;height:32px;border-radius:16px;background:var(--navy);color:#fff;font-size:9.5px}
.tx::before{content:"";position:absolute;left:-7px;top:10px;border-right:8px solid var(--navy);border-top:6px solid transparent;border-bottom:6px solid transparent}
.tx .d{position:absolute;left:11px;top:9px}
.tx .v{position:absolute;right:12px;top:9px}
.dot{left:16px;width:8px;height:8px;border-radius:50%;background:var(--navy)}

/* dashboard */
.menu-card{left:30px;width:273px;height:65px;background:#fff;border-radius:12px;box-shadow:0 2px 6px rgba(20,40,90,.08)}
.menu-icon{position:absolute;left:0;top:0;width:47px;height:65px;background:var(--navy);border-radius:12px 0 0 12px}
.menu-icon svg{position:absolute;left:12px;top:20px}
.menu-label{position:absolute;left:69px;top:25px;font-size:10.5px;color:var(--navy)}

/* profile */
.profile-photo{left:108px;top:45px;width:116px;height:116px;border-radius:50%;background:radial-gradient(circle at 50% 45%,#e2c3a8 0%,#a9765a 45%,#3a2620 100%);border:3px solid #fff}
.profile-name{left:0;top:170px;width:100%;text-align:center;font-size:19px;color:var(--navy)}
.field{height:35px;background:var(--field);border-radius:8px;font-size:13px;color:var(--ink);padding:9px 0 0 13px}
.field .ok{position:absolute;right:12px;top:11px}
.save-btn{left:18px;top:583px;width:297px;height:35px;background:var(--navy);border-radius:8px;color:#fff;font-size:13px;text-align:center;line-height:35px}

/* auth */
.auth-photo{left:0;top:23px;width:100%;height:622px;background:linear-gradient(160deg,#7f8bad 0%,#8a9cc6 40%,#6b7fae 75%,#8798c2 100%)}
.auth-foot{left:0;top:645px;width:100%;height:77px;background:#7486b0}
.brand{left:90px;top:83px;color:#fff;font-size:19px;line-height:21px;letter-spacing:.5px}
.brand i{position:absolute;left:0;top:4px;width:34px;height:34px;border-radius:6px;background:#e45b6a}
.brand span{position:absolute;left:70px;top:0;width:120px}
.auth-card{left:20px;top:250px;width:296px;background:#fff;border-radius:16px}
.tabs{left:49px;top:233px;width:238px;height:32px;border-radius:4px 4px 0 0;overflow:hidden;display:flex;box-shadow:0 2px 5px rgba(0,0,0,.15)}
.tabs div{flex:1;text-align:center;font-size:9px;line-height:32px;color:#fff;background:var(--tab-off)}
.tabs .on{background:var(--navy)}
.flabel{left:66px;font-size:7.5px;color:var(--ink)}
.flabel svg{position:absolute;left:-16px;top:-3px}
.afield{left:49px;width:238px;height:35px;background:var(--field);border-radius:8px;font-size:13px;color:var(--ink);padding:8px 0 0 14px}
.btn{left:67px;width:201px;height:35px;background:var(--black);border-radius:8px;color:#fff;font-size:13px;text-align:center;line-height:35px}
.forgot{left:180px;top:441px;font-size:7px;color:var(--ink);letter-spacing:.3px}
</style>
</head>
<body>
<div class="canvas">
<div class="stage">

  <!-- background shapes -->
  <div class="blob" style="left:250px;top:22px;width:160px;height:160px"></div>
  <div class="blob" style="left:1053px;top:38px;width:170px;height:170px"></div>
  <div class="blob" style="left:800px;top:180px;width:420px;height:420px"></div>
  <div class="blob" style="left:-55px;top:515px;width:110px;height:110px"></div>
  <div class="blob" style="left:563px;top:885px;width:162px;height:162px"></div>
  <div class="blob" style="left:1365px;top:877px;width:28px;height:28px"></div>
  <div class="blob" style="left:1917px;top:1018px;width:98px;height:98px"></div>
  <div class="blob" style="left:-330px;top:1090px;width:960px;height:1100px"></div>
  <div class="blob" style="left:1600px;top:-420px;width:900px;height:1130px"></div>
  <div class="blob" style="left:1450px;top:1450px;width:900px;height:800px"></div>

  <!-- HOME -->
  <section class="phone" style="left:176px;top:104px">
    <div class="header"><div class="avatar"></div><div class="user-name">Clara Whitfield</div>
      <svg class="gear" width="24" height="24" viewBox="0 0 24 24" fill="none" stroke="#fff" stroke-width="1.6"><circle cx="12" cy="12" r="4"/><circle cx="12" cy="12" r="8.5" stroke-dasharray="3 2"/></svg></div>
    <div class="status">12:30<svg width="52" height="11" viewBox="0 0 52 11"><path d="M0 10 L10 0 V10Z" fill="#fff"/><path d="M14 1 H28 L21 10Z" fill="#fff"/><rect x="36" y="1" width="15" height="9" rx="1.5" fill="#fff"/></svg></div>
    <div class="panel">
    </div>
    <div class="abs balance-card"></div>
    <svg class="abs" style="left:108px;top:121px" width="40" height="36" viewBox="0 0 40 36" fill="none" stroke="#1a3a78" stroke-width="1.6"><rect x="2" y="6" width="32" height="24" rx="3"/><path d="M2 10 H30"/><rect x="24" y="16" width="12" height="8" rx="2"/><circle cx="30" cy="30" r="4"/></svg>
    <div class="abs balance-amount">180,999 $</div>
    <div class="abs balance-label">Balance</div>
    <div class="abs progress"><span></span></div>
    <div class="abs flow income">
      <svg width="26" height="34" viewBox="0 0 26 34" fill="none" stroke="#fff" stroke-width="1.4"><circle cx="13" cy="22" r="10"/><path d="M13 16 V28 M10 19 H15 a2 2 0 0 1 0 3 H11 a2 2 0 0 0 0 3 H16"/><path d="M7 9 V2 M13 9 V0 M19 9 V3 M5 4 L7 2 L9 4 M11 2 L13 0 L15 2"/></svg>
      <div class="amt">109,999 $</div><div class="lbl">Income</div></div>
    <div class="abs flow expense">
      <svg width="36" height="34" viewBox="0 0 36 34" fill="none" stroke="#fff" stroke-width="1.4"><circle cx="8" cy="8" r="6"/><rect x="3" y="12" width="30" height="16" rx="2"/><circle cx="18" cy="20" r="5"/><path d="M6 28 v4 M12 28 v4 M24 28 v4 M30 28 v4"/></svg>
      <div class="amt">071,000 $</div><div class="lbl">Expense</div></div>

    <div class="abs section-head" style="top:277px"><div class="section-title">Expense</div><div class="view-all">View All</div></div>
    <div class="abs section-body" style="top:315px;height:173px"></div>
    <div class="abs row-card" style="top:331px"><div class="row-icon"><svg width="16" height="16" viewBox="0 0 16 16" fill="#1a3a78"><path d="M2 6 H14 L12.5 15 H3.5Z"/><path d="M5 6 V4 a3 3 0 0 1 6 0 V6" fill="none" stroke="#1a3a78" stroke-width="1.4"/></svg></div><div class="row-title">Shopping</div><div class="row-amt">199$</div>
      <svg class="row-go" width="20" height="20" viewBox="0 0 20 20" fill="none" stroke="#1a3a78" stroke-width="1.5"><circle cx="10" cy="10" r="8.5"/><path d="M8.5 6 L12.5 10 L8.5 14"/></svg></div>
    <div class="abs row-card" style="top:408px"><div class="row-icon"><svg width="16" height="16" viewBox="0 0 16 16" fill="#1a3a78"><rect x="1" y="4" width="14" height="9" rx="4.5"/><path d="M4 7.5 h3 M5.5 6 v3" stroke="#fff" stroke-width="1.2"/><circle cx="11" cy="7" r="1" fill="#fff"/><circle cx="12.5" cy="9" r="1" fill="#fff"/></svg></div><div class="row-title">Video Games</div><div class="row-amt">500$</div>
      <svg class="row-go" width="20" height="20" viewBox="0 0 20 20" fill="none" stroke="#1a3a78" stroke-width="1.5"><circle cx="10" cy="10" r="8.5"/><path d="M8.5 6 L12.5 10 L8.5 14"/></svg></div>

    <div class="abs section-head" style="top:498px"><div class="section-title">Report</div><div class="view-all">View All</div></div>
    <div class="abs section-body" style="top:535px;height:200px"></div>
    <div class="abs row-card" style="top:551px"><div class="row-icon"><svg width="16" height="16" viewBox="0 0 16 16" fill="none" stroke="#1a3a78" stroke-width="1.3"><path d="M1 10 L5 6 L8 8 L14 2 M1 13 H15 M1 15 H15"/></svg></div><div class="row-title" style="top:18px">Today’s Report</div><div class="row-sub">Lorem ipsum</div>
      <div class="trend" style="top:21px"><b style="color:#1f8a3e">↑</b>250$</div><div class="trend" style="top:32px"><b style="color:#e0203a">↓</b>199$</div>
      <svg class="row-go" width="20" height="20" viewBox="0 0 20 20" fill="none" stroke="#1a3a78" stroke-width="1.5"><circle cx="10" cy="10" r="8.5"/><path d="M8.5 6 L12.5 10 L8.5 14"/></svg></div>
    <div class="abs row-card" style="top:628px"><div class="row-icon"><svg width="16" height="16" viewBox="0 0 16 16" fill="none" stroke="#1a3a78" stroke-width="1.3"><path d="M1 10 L5 6 L8 8 L14 2"/></svg></div><div class="row-title" style="top:18px">17-9-2020’s Report</div>
      <div class="trend" style="top:21px"><b style="color:#1f8a3e">↑</b>500$</div></div>

    <nav class="navbar">
      <div class="nav-item active" style="left:47px"><svg width="22" height="20" viewBox="0 0 22 20" fill="none" stroke="#1a3a78" stroke-width="1.4"><path d="M2 10 L11 2 L20 10 M5 8 V19 H17 V8"/><rect x="9" y="12" width="4" height="7"/></svg>Home</div>
      <div class="nav-item" style="left:101px"><svg width="22" height="20" viewBox="0 0 22 20" fill="none" stroke="#222" stroke-width="1.3"><circle cx="11" cy="11" r="7"/><path d="M11 7 V11 L14 13 M9 2 H13"/></svg>History</div>
      <div class="nav-add"></div>
      <div class="nav-item" style="left:228px"><svg width="22" height="22" viewBox="0 0 22 22" fill="none" stroke="#222" stroke-width="1.2"><rect x="2" y="2" width="18" height="18" rx="2"/><path d="M7 5 V17 M11 5 V17 M15 5 V17"/><rect x="5.5" y="8" width="3" height="2"/><rect x="9.5" y="12" width="3" height="2"/><rect x="13.5" y="7" width="3" height="2"/></svg>Dashboard</div>
      <div class="nav-item" style="left:286px"><svg width="22" height="20" viewBox="0 0 22 20" fill="none" stroke="#222" stroke-width="1.3"><circle cx="11" cy="10" r="9"/><circle cx="11" cy="8" r="3"/><path d="M5 16 a7 5 0 0 1 12 0"/></svg>Profile</div>
    </nav>
  </section>

  <!-- HISTORY -->
  <section class="phone" style="left:868px;top:104px">
    <div class="header"><div class="avatar"></div><div class="user-name">Clara Whitfield</div>
      <svg class="gear" width="24" height="24" viewBox="0 0 24 24" fill="none" stroke="#fff" stroke-width="1.6"><circle cx="12" cy="12" r="4"/><circle cx="12" cy="12" r="8.5" stroke-dasharray="3 2"/></svg></div>
    <div class="status">12:30<svg width="52" height="11" viewBox="0 0 52 11"><path d="M0 10 L10 0 V10Z" fill="#fff"/><path d="M14 1 H28 L21 10Z" fill="#fff"/><rect x="36" y="1" width="15" height="9" rx="1.5" fill="#fff"/></svg></div>
    <div class="panel"></div>
    <div class="abs timeline"></div>
    <div class="abs tx" style="top:110px"><span class="d">Thursday, September 17 - 2020</span><span class="v">150 $</span></div><div class="abs dot" style="top:122px"></div>
    <div class="abs tx" style="top:151px"><span class="d">Thursday, September 17 - 2020</span><span class="v">150 $</span></div><div class="abs dot" style="top:163px"></div>
    <div class="abs tx" style="top:193px"><span class="d">Thursday, September 17 - 2020</span><span class="v">150 $</span></div><div class="abs dot" style="top:205px"></div>
    <div class="abs tx" style="top:234px"><span class="d">Thursday, September 17 - 2020</span><span class="v">150 $</span></div><div class="abs dot" style="top:246px"></div>
    <div class="abs tx" style="top:276px"><span class="d">Thursday, September 17 - 2020</span><span class="v">150 $</span></div><div class="abs dot" style="top:288px"></div>
    <div class="abs tx" style="top:317px"><span class="d">Thursday, September 17 - 2020</span><span class="v">150 $</span></div><div class="abs dot" style="top:329px"></div>
    <div class="abs tx" style="top:358px"><span class="d">Thursday, September 17 - 2020</span><span class="v">150 $</span></div><div class="abs dot" style="top:370px"></div>
    <div class="abs tx" style="top:400px"><span class="d">Thursday, September 17 - 2020</span><span class="v">150 $</span></div><div class="abs dot" style="top:412px"></div>
    <div class="abs tx" style="top:441px"><span class="d">Thursday, September 17 - 2020</span><span class="v">150 $</span></div><div class="abs dot" style="top:453px"></div>
    <div class="abs tx" style="top:483px"><span class="d">Thursday, September 17 - 2020</span><span class="v">150 $</span></div><div class="abs dot" style="top:495px"></div>
    <div class="abs tx" style="top:524px"><span class="d">Thursday, September 17 - 2020</span><span class="v">150 $</span></div><div class="abs dot" style="top:536px"></div>
    <div class="abs tx" style="top:566px"><span class="d">Thursday, September 17 - 2020</span><span class="v">150 $</span></div><div class="abs dot" style="top:578px"></div>
    <div class="abs tx" style="top:607px"><span class="d">Thursday, September 17 - 2020</span><span class="v">150 $</span></div><div class="abs dot" style="top:619px"></div>
    <div class="abs tx" style="top:648px"></div>
    <nav class="navbar">
      <div class="nav-item" style="left:47px"><svg width="22" height="20" viewBox="0 0 22 20" fill="none" stroke="#222" stroke-width="1.4"><path d="M2 10 L11 2 L20 10 M5 8 V19 H17 V8"/><rect x="9" y="12" width="4" height="7"/></svg>Home</div>
      <div class="nav-item active" style="left:101px"><svg width="22" height="20" viewBox="0 0 22 20" fill="none" stroke="#1a3a78" stroke-width="1.3"><circle cx="11" cy="11" r="7"/><path d="M11 7 V11 L14 13 M9 2 H13"/></svg>History</div>
      <div class="nav-add"></div>
      <div class="nav-item" style="left:228px"><svg width="22" height="22" viewBox="0 0 22 22" fill="none" stroke="#222" stroke-width="1.2"><rect x="2" y="2" width="18" height="18" rx="2"/><path d="M7 5 V17 M11 5 V17 M15 5 V17"/></svg>Dashboard</div>
      <div class="nav-item" style="left:286px"><svg width="22" height="20" viewBox="0 0 22 20" fill="none" stroke="#222" stroke-width="1.3"><circle cx="11" cy="10" r="9"/><circle cx="11" cy="8" r="3"/><path d="M5 16 a7 5 0 0 1 12 0"/></svg>Profile</div>
    </nav>
  </section>

  <!-- DASHBOARD -->
  <section class="phone" style="left:1560px;top:104px">
    <div class="header"><div class="avatar"></div><div class="user-name">Clara Whitfield</div>
      <svg class="gear" width="24" height="24" viewBox="0 0 24 24" fill="none" stroke="#fff" stroke-width="1.6"><circle cx="12" cy="12" r="4"/><circle cx="12" cy="12" r="8.5" stroke-dasharray="3 2"/></svg></div>
    <div class="status">12:30<svg width="52" height="11" viewBox="0 0 52 11"><path d="M0 10 L10 0 V10Z" fill="#fff"/><path d="M14 1 H28 L21 10Z" fill="#fff"/><rect x="36" y="1" width="15" height="9" rx="1.5" fill="#fff"/></svg></div>
    <div class="panel"></div>
    <div class="abs menu-card" style="top:127px"><div class="menu-icon"><svg width="24" height="24" viewBox="0 0 24 24" fill="none" stroke="#fff" stroke-width="1.4"><rect x="2" y="4" width="12" height="16"/><path d="M5 8 h6 M5 12 h6 M5 16 h6"/><circle cx="19" cy="7" r="3"/></svg></div><div class="menu-label">Manage Month Income</div></div>
    <div class="abs menu-card" style="top:207px"><div class="menu-icon"><svg width="24" height="24" viewBox="0 0 24 24" fill="none" stroke="#fff" stroke-width="1.4"><rect x="6" y="2" width="14" height="18"/><path d="M9 6 h8 M9 10 h8 M9 14 h5"/><circle cx="6" cy="18" r="4"/></svg></div><div class="menu-label">Manage Recurring Expenses</div></div>
    <div class="abs menu-card" style="top:287px"><div class="menu-icon"><svg width="24" height="24" viewBox="0 0 24 24" fill="none" stroke="#fff" stroke-width="1.6"><circle cx="7" cy="7" r="4.5"/><circle cx="17" cy="7" r="4.5"/><path d="M5 15 q7 8 14 0"/></svg></div><div class="menu-label">Manage Monthly Budgets</div></div>
    <div class="abs menu-card" style="top:367px"><div class="menu-icon"><svg width="24" height="24" viewBox="0 0 24 24" fill="none" stroke="#fff" stroke-width="1.4"><path d="M2 20 H22 M5 20 V14 M10 20 V11 M15 20 V13 M20 20 V8 M4 10 L10 6 L14 8 L21 3"/></svg></div><div class="menu-label">Manage Monthly Savings/Investments</div></div>
    <div class="abs menu-card" style="top:447px"><div class="menu-icon"><svg width="24" height="24" viewBox="0 0 24 24" fill="none" stroke="#fff" stroke-width="1.5"><circle cx="12" cy="7" r="5"/><path d="M2 16 h6 l4 3 h8 M2 22 h18"/></svg></div><div class="menu-label">Auto Expenses</div></div>
    <div class="abs menu-card" style="top:527px"><div class="menu-icon"><svg width="24" height="24" viewBox="0 0 24 24" fill="none" stroke="#fff" stroke-width="1.5"><path d="M4 12 a8 8 0 0 1 14 -5 M20 12 a8 8 0 0 1 -14 5"/><path d="M18 3 v4 h-4 M6 21 v-4 h4"/><path d="M12 7 V17 M14.5 9.5 H11 a1.8 1.8 0 0 0 0 3.5 h2 a1.8 1.8 0 0 1 0 3.5 H9.5"/></svg></div><div class="menu-label">Auto Income Credit</div></div>
    <nav class="navbar">
      <div class="nav-item" style="left:47px"><svg width="22" height="20" viewBox="0 0 22 20" fill="none" stroke="#222" stroke-width="1.4"><path d="M2 10 L11 2 L20 10 M5 8 V19 H17 V8"/><rect x="9" y="12" width="4" height="7"/></svg>Home</div>
      <div class="nav-item" style="left:101px"><svg width="22" height="20" viewBox="0 0 22 20" fill="none" stroke="#222" stroke-width="1.3"><circle cx="11" cy="11" r="7"/><path d="M11 7 V11 L14 13 M9 2 H13"/></svg>History</div>
      <div class="nav-add"></div>
      <div class="nav-item active" style="left:228px"><svg width="22" height="22" viewBox="0 0 22 22" fill="none" stroke="#1a3a78" stroke-width="1.2"><rect x="2" y="2" width="18" height="18" rx="2"/><path d="M7 5 V17 M11 5 V17 M15 5 V17"/></svg>Dashboard</div>
      <div class="nav-item" style="left:286px"><svg width="22" height="20" viewBox="0 0 22 20" fill="none" stroke="#222" stroke-width="1.3"><circle cx="11" cy="10" r="9"/><circle cx="11" cy="8" r="3"/><path d="M5 16 a7 5 0 0 1 12 0"/></svg>Profile</div>
    </nav>
  </section>

  <!-- PROFILE -->
  <section class="phone" style="left:176px;top:938px">
    <div class="header"></div>
    <div class="status">12:30<svg width="52" height="11" viewBox="0 0 52 11"><path d="M0 10 L10 0 V10Z" fill="#fff"/><path d="M14 1 H28 L21 10Z" fill="#fff"/><rect x="36" y="1" width="15" height="9" rx="1.5" fill="#fff"/></svg></div>
    <div class="panel"></div>
    <div class="abs profile-photo" role="img" aria-label="Profile photo of the user"></div>
    <div class="abs profile-name">Clara Whitfield</div>
    <div class="abs field" style="left:18px;top:250px;width:141px">Clara</div>
    <div class="abs field" style="left:173px;top:250px;width:142px">Whitfield</div>
    <div class="abs field" style="left:18px;top:297px;width:297px">ClaraWhitfield@mailbox.com<svg class="ok" width="12" height="12" viewBox="0 0 12 12" fill="none" stroke="#8bbf3a" stroke-width="1.1"><circle cx="6" cy="6" r="5"/><path d="M3.5 6 L5.5 8 L10 3"/></svg></div>
    <div class="abs field" style="left:18px;top:344px;width:297px">+99 999-999-9999<svg class="ok" width="12" height="12" viewBox="0 0 12 12" fill="none" stroke="#8bbf3a" stroke-width="1.1"><circle cx="6" cy="6" r="5"/><path d="M3.5 6 L5.5 8 L10 3"/></svg></div>
    <div class="abs field" style="left:18px;top:392px;width:297px">393939393939393939<svg class="ok" width="12" height="12" viewBox="0 0 12 12" fill="none" stroke="#8bbf3a" stroke-width="1.1"><circle cx="6" cy="6" r="5"/><path d="M3.5 6 L5.5 8 L10 3"/></svg></div>
    <div class="abs field" style="left:18px;top:439px;width:297px">Other information</div>
    <div class="abs field" style="left:18px;top:487px;width:297px">Other information</div>
    <div class="abs field" style="left:18px;top:534px;width:297px">Other information</div>
    <div class="abs save-btn">Save Changes</div>
    <nav class="navbar">
      <div class="nav-item" style="left:47px"><svg width="22" height="20" viewBox="0 0 22 20" fill="none" stroke="#222" stroke-width="1.4"><path d="M2 10 L11 2 L20 10 M5 8 V19 H17 V8"/><rect x="9" y="12" width="4" height="7"/></svg>Home</div>
      <div class="nav-item" style="left:101px"><svg width="22" height="20" viewBox="0 0 22 20" fill="none" stroke="#222" stroke-width="1.3"><circle cx="11" cy="11" r="7"/><path d="M11 7 V11 L14 13 M9 2 H13"/></svg>History</div>
      <div class="nav-add"></div>
      <div class="nav-item" style="left:228px"><svg width="22" height="22" viewBox="0 0 22 22" fill="none" stroke="#222" stroke-width="1.2"><rect x="2" y="2" width="18" height="18" rx="2"/><path d="M7 5 V17 M11 5 V17 M15 5 V17"/></svg>Dashboard</div>
      <div class="nav-item active" style="left:286px"><svg width="22" height="20" viewBox="0 0 22 20" fill="none" stroke="#1a3a78" stroke-width="1.3"><circle cx="11" cy="10" r="9"/><circle cx="11" cy="8" r="3"/><path d="M5 16 a7 5 0 0 1 12 0"/></svg>Profile</div>
    </nav>
  </section>

  <!-- LOGIN -->
  <section class="phone" style="left:880px;top:938px">
    <div class="abs auth-photo" role="img" aria-label="Photo of a smartphone and calendar pages on a desk"></div>
    <div class="abs auth-foot"></div>
    <div class="status" style="background:rgba(15,42,85,.75)">12:30<svg width="52" height="11" viewBox="0 0 52 11"><path d="M0 10 L10 0 V10Z" fill="#fff"/><path d="M14 1 H28 L21 10Z" fill="#fff"/><rect x="36" y="1" width="15" height="9" rx="1.5" fill="#fff"/></svg></div>
    <div class="abs brand"><i></i><span>Expenses Tracker</span></div>
    <div class="abs auth-card" style="height:330px"></div>
    <div class="abs tabs"><div class="on">Login</div><div>Register</div></div>
    <div class="abs flabel" style="top:296px"><svg width="12" height="10" viewBox="0 0 12 10" fill="none" stroke="#222" stroke-width="1"><rect x=".5" y=".5" width="11" height="9"/><path d="M.5 .5 L6 5 L11.5 .5"/></svg>Email</div>
    <div class="abs afield" style="top:313px">ClaraWhitfield@mailbox.com</div>
    <div class="abs flabel" style="top:379px"><svg width="10" height="12" viewBox="0 0 10 12" fill="none" stroke="#222" stroke-width="1"><rect x=".5" y="5" width="9" height="6.5"/><path d="M2.5 5 V3 a2.5 2.5 0 0 1 5 0 V5"/></svg>Password</div>
    <div class="abs afield" style="top:396px;letter-spacing:1px">**********************</div>
    <div class="abs forgot" style="left:192px">FORGOT PASSWORD?</div>
    <div class="abs btn" style="top:473px">Login</div>
    <div class="abs btn" style="top:518px">Login With Circlebook</div>
  </section>

  <!-- REGISTER -->
  <section class="phone" style="left:1572px;top:938px">
    <div class="abs auth-photo" role="img" aria-label="Photo of a smartphone and calendar pages on a desk"></div>
    <div class="abs auth-foot"></div>
    <div class="status" style="background:rgba(15,42,85,.75)">12:30<svg width="52" height="11" viewBox="0 0 52 11"><path d="M0 10 L10 0 V10Z" fill="#fff"/><path d="M14 1 H28 L21 10Z" fill="#fff"/><rect x="36" y="1" width="15" height="9" rx="1.5" fill="#fff"/></svg></div>
    <div class="abs brand"><i></i><span>Expenses Tracker</span></div>
    <div class="abs auth-card" style="height:398px"></div>
    <div class="abs tabs"><div>Login</div><div class="on">Register</div></div>
    <div class="abs flabel" style="top:296px"><svg width="12" height="12" viewBox="0 0 12 12" fill="none" stroke="#222" stroke-width="1"><circle cx="6" cy="6" r="5.5"/><circle cx="6" cy="5" r="2"/><path d="M2.5 10 a4 3 0 0 1 7 0"/></svg>User Name</div>
    <div class="abs afield" style="top:313px">Clara Whitfield</div>
    <div class="abs flabel" style="top:379px"><svg width="12" height="10" viewBox="0 0 12 10" fill="none" stroke="#222" stroke-width="1"><rect x=".5" y=".5" width="11" height="9"/><path d="M.5 .5 L6 5 L11.5 .5"/></svg>Email</div>
    <div class="abs afield" style="top:396px">ClaraWhitfield@mailbox.com</div>
    <div class="abs flabel" style="top:463px"><svg width="10" height="12" viewBox="0 0 10 12" fill="none" stroke="#222" stroke-width="1"><rect x=".5" y="5" width="9" height="6.5"/><path d="M2.5 5 V3 a2.5 2.5 0 0 1 5 0 V5"/></svg>Password</div>
    <div class="abs afield" style="top:480px;letter-spacing:1px">**********************</div>
    <div class="abs btn" style="top:542px">Register</div>
    <div class="abs btn" style="top:586px">Register With Circlebook</div>
  </section>

</div>
</div>
</body>
</html>
```